Information Technology Business Needs Flyer Design

We need a flyer design for an IT business called SILVERFERN Technology based in Darwin, Northern Territory Australia. Flyers will be printed and distributed to residential and commercial properties. For more information about the business, please visit www.silverferntech-example.com.au

We are after an original, eye catching design that portrays information about our services. Design should be clean and simple, not overly cluttered.

Our logo can be found on our website. The font used is EURO-STILE.

Contact me for high res media if needed.

Industry/Entity Type

Residential

Requirements
Must have
• Used EURO-STILE as font.
• SILVERFERN Technology logo found on Website.

```html
<!DOCTYPE html>
<html lang="en">
<head>
<meta charset="utf-8">
<title>SILVERFERN Technology – IT Services Flyer</title>
<link rel="stylesheet" href="https://fonts.googleapis.com/css2?family=Titillium+Web:wght@300;400;600;700&display=swap">
<style>
  :root {
    --ink: #231f20;
    --charcoal: #5b5b5d;
    --slate: #8a8a8c;
    --mist: #bdbdbf;
    --red: #e31e24;
    --salmon: #f5a98f;
    --white: #ffffff;
    --page: #ffffff;
  }
  * { box-sizing: border-box; margin: 0; padding: 0; }
  html, body { width: 1200px; height: 1200px; overflow: hidden; background: var(--page); }
  body { font-family: "Titillium Web", "Helvetica Neue", Arial, sans-serif; color: var(--ink); position: relative; }

  .flyer {
    position: absolute; left: 219px; top: 60px; width: 762px; height: 1078px;
    background: var(--white);
    box-shadow: 3px 4px 8px rgba(0,0,0,0.35);
    overflow: hidden;
  }
  .block { position: absolute; }

  .headline { left: 0; top: 0; width: 379px; height: 190px; background: var(--ink); color: var(--white); padding: 24px 20px 0 21px; }
  .headline h1 { font-size: 23px; font-weight: 600; line-height: 30px; letter-spacing: 0.3px; }
  .headline p { font-size: 21.5px; font-weight: 300; line-height: 30px; }

  .photo { background: linear-gradient(160deg, #eef0f2 0%, #c9cdd2 45%, #8c7466 75%, #dcdfe2 100%); }
  .photo-handshake { left: 379px; top: 0; width: 191px; height: 190px; }
  .photo-desk { left: 0; top: 570px; width: 570px; height: 385px;
    background: linear-gradient(100deg, #e9ecef 0%, #d6c3a3 30%, #f3f4f5 55%, #e8eaec 80%, #c9ccd0 100%); }

  .site-band { left: 570px; top: 0; width: 192px; height: 379px; background: var(--charcoal); }
  .site-url { position: absolute; left: 150px; top: 24px; writing-mode: vertical-rl; color: var(--white); font-size: 21px; font-weight: 300; letter-spacing: 0.3px; white-space: nowrap; }

  .intro { left: 0; top: 190px; width: 379px; height: 189px; background: var(--mist); padding: 28px 20px 0 21px; }
  .intro p { font-size: 17.5px; line-height: 29px; color: var(--ink); white-space: nowrap; }

  .brand-tile { left: 0; top: 379px; width: 191px; height: 191px; background: var(--white); display: flex; align-items: center; justify-content: center; }
  .brand-tile span { font-size: 22px; font-weight: 700; color: var(--ink); letter-spacing: 0.5px; }
  .accent-tile { left: 191px; top: 379px; width: 188px; height: 191px; background: var(--salmon); }
  .veil-tile { left: 0; top: 570px; width: 191px; height: 190px; background: rgba(120,120,122,0.55); }

  .services { left: 379px; top: 190px; width: 191px; height: 570px; background: var(--red); color: var(--white); padding: 34px 8px 0 13px; }
  .solutions { left: 570px; top: 379px; width: 192px; height: 576px; background: var(--slate); color: var(--white); padding: 46px 8px 0 12px; }

  .group-title { font-size: 18.5px; font-weight: 400; letter-spacing: 2.2px; line-height: 24px; margin-bottom: 9px; }
  .group + .group { margin-top: 26px; }
  .solutions .group + .group { margin-top: 34px; }
  .items { list-style: none; }
  .items li { position: relative; font-size: 14.2px; line-height: 20px; padding-left: 14px; margin-bottom: 10px; white-space: nowrap; }
  .items li::before {
    content: ""; position: absolute; left: 1px; top: 5px;
    border-left: 7px solid var(--white); border-top: 4.5px solid transparent; border-bottom: 4.5px solid transparent;
  }
  .solutions .items li::before { border-left-color: var(--red); }

  .footer { left: 0; top: 955px; width: 762px; height: 123px; background: var(--white); }
  .footer-brand { position: absolute; left: 20px; top: 44px; display: flex; align-items: center; gap: 10px; }
  .footer-brand i { width: 24px; height: 24px; background: var(--ink); display: block; }
  .footer-brand span { font-size: 25px; font-weight: 700; color: var(--ink); letter-spacing: 0.4px; white-space: nowrap; }
  .contact { position: absolute; left: 392px; top: 24px; white-space: nowrap; }
  .contact .call { font-size: 21px; font-weight: 400; color: var(--ink); letter-spacing: 0.5px; line-height: 40px; }
  .contact .call strong { font-size: 33px; font-weight: 700; color: var(--red); letter-spacing: 2px; margin-left: 4px; }
  .contact .email { font-size: 17.5px; font-weight: 400; color: var(--ink); line-height: 26px; }
</style>
</head>
<body>
  <main class="flyer">
    <section class="block headline">
      <h1>YOUR LOCAL COMPREHENSIVE<br>IT SOLUTIONS PROVIDER</h1>
      <p>for both residential and<br>commercial sectors with over<br>10 years experience.</p>
    </section>

    <div class="block photo photo-handshake" role="img" aria-label="Photo of a business handshake"></div>

    <aside class="block site-band">
      <span class="site-url">www.silverferntech-example.com.au</span>
    </aside>

    <section class="block intro">
      <p>With vast knowledge across the industry,<br>we can provide what you are looking for,<br>delivering responsive, reliable and<br>effective IT solutions.</p>
    </section>

    <div class="block brand-tile"><span>SILVERFERN</span></div>
    <div class="block accent-tile"></div>

    <div class="block photo photo-desk" role="img" aria-label="Photo of a smiling woman working on a laptop at a desk"></div>
    <div class="block veil-tile"></div>

    <section class="block services">
      <div class="group">
        <h2 class="group-title">IT SERVICES</h2>
        <ul class="items">
          <li>Hardware Sales</li>
          <li>VPN \ Remote Access</li>
          <li>System Integrations</li>
          <li>Network Server<br>Installation</li>
          <li>Antivirus &amp; SPAM</li>
          <li>Retail Systems</li>
        </ul>
      </div>
      <div class="group">
        <h2 class="group-title">TECHNICAL<br>SUPPORT</h2>
        <ul class="items">
          <li>PC \ Laptop Support</li>
          <li>Server Support</li>
          <li>Networking</li>
          <li>Business on-site<br>Support</li>
          <li>Virus \ SPAM Removal</li>
        </ul>
      </div>
    </section>

    <section class="block solutions">
      <div class="group">
        <h2 class="group-title">IT SOLUTIONS</h2>
        <ul class="items">
          <li>System Monitoring</li>
          <li>System Administration</li>
          <li>Network Server<br>Maintenance</li>
          <li>Backup Solutions</li>
          <li>Infrastructure<br>Consultation, Design<br>and Implementation</li>
        </ul>
      </div>
      <div class="group">
        <h2 class="group-title">WEB PRESENCE</h2>
        <ul class="items">
          <li>Find new customers<br>and grow your<br>customer base</li>
          <li>Grow your revenue<br>and profits</li>
          <li>Let your customers<br>find your business<br>with ease</li>
        </ul>
      </div>
    </section>

    <footer class="block footer">
      <div class="footer-brand"><i></i><span>SILVERFERN Technology</span></div>
      <div class="contact">
        <p class="call">CALL: <strong>0400 555 018</strong></p>
        <p class="email">enquiries@silverferntech-example.com.au</p>
      </div>
    </footer>
  </main>
</body>
</html>
```